KLD Photography Editing & Support Services for Real Estate

We require a double sided A4 flyer to promote our photography services to real estate agencies.
This particular service is targeted to rural areas where reliable, professional and highly skilled photographers are difficult to source. We teach the agent how to photograph, they upload files to a server and we take care of the rest (image editing, quality control and delivery). This will give the agents flexibility with when to shoot and eliminates the stress of managing a photographer / contractor. We offer a 1 day face to face training session and competitive packages for equipment start up.
We would like the flyer to look clean & very professional. The flyer should showcase samples of our work to highlight what can be achieved by using our services. We like the look of a black or dark background behind the text and feel that would look nice with our photographs provided. Otherwise open to your suggestions and ideas.
TEXT FOR FLYER:
Welcome to the KLD Real Estate Photography Editing and Support Service
• Take your real estate business to the next level by providing impressive real estate imagery that makes you stands out from the competition
• Omit the stress of trying to find a good photographer or managing an unreliable one and hence have more time to focus on other aspects of your business
• Showcase your listings with better quality and more impactful photographs than your competitors thereby increasing potential for a quick sale
• Great first impressions matter and you will achieve this by looking and feeling more professional. This will attract and retain more future clients.
HOW IT WORKS
• We understand that your time is valuable, so let us handle the editing and delivery of your images. You shoot, and we take care of the rest.
• Images are edited and delivered within 1 working day
INCLUSIONS:
• Full day face to face training (we come to you) and instructional handbook
• We will teach you everything you need to know about your equipment and how to take stunning real estate photographs
• Service turnaround within 1 working day
• Free HELP desk service Mon-Fri
• 12 month Exclusivity (rural towns only) for a limited time
INVESTMENT
• 99 per listing for us to manage images including editing, quality control and delivery (10 Images)
• Ask us about competitive packages for photography equipment if required
SUMMARY
The KLD Real Estate Photography Editing and Support Service is the perfect solution for busy real estate professionals who want to take their business to the next level. Our service is affordable, flexible, and designed to help you showcase your listings in the best possible light.
Contact us today to learn more about how we can help you.

```html
<!DOCTYPE html>
<html lang="en">
<head>
<meta charset="utf-8">
<title>KLD Real Estate Photography Editing and Support Service – Flyer</title>
<link rel="stylesheet" href="https://fonts.googleapis.com/css2?family=EB+Garamond:wght@400&family=Montserrat:wght@300;400&display=swap">
<style>
  :root {
    --backdrop: #e4e4e2;
    --charcoal: #2c2c2d;
    --orange: #f07124;
    --white: #ffffff;
    --body-grey: #5a5a5a;
    --brand-grey: #c9c9c9;
    --serif: "EB Garamond", "Times New Roman", serif;
    --sans: "Montserrat", Arial, sans-serif;
  }
  * { box-sizing: border-box; margin: 0; padding: 0; }
  html, body { width: 1200px; height: 900px; overflow: hidden; }
  body { background: var(--backdrop); position: relative; font-family: var(--sans); }

  .page {
    position: absolute; top: 54px; width: 560px; height: 792px;
    background: var(--charcoal); overflow: hidden;
  }
  .page--front { left: 25px; }
  .page--back { left: 615px; }

  .brand {
    position: absolute; top: 0; left: 0; width: 100%; height: 104px;
    display: flex; align-items: center; justify-content: center;
  }
  .brand__name {
    font-family: var(--sans); font-weight: 300; font-size: 22px;
    letter-spacing: 6px; color: var(--brand-grey);
  }

  .accent-bar {
    position: absolute; top: 103px; left: 0; width: 275px; height: 8px;
    background: var(--orange);
    clip-path: polygon(0 0, 96% 0, 100% 100%, 0 100%);
  }

  .hero { position: absolute; top: 111px; left: 0; width: 100%; height: 274px; }
  .hero--lounge { background: linear-gradient(180deg, #2f4f78 0%, #6b5a46 45%, #8a6e52 70%, #4a4440 100%); }
  .hero--kitchen { background: linear-gradient(180deg, #d9d7d2 0%, #f1efeb 40%, #b59a7c 75%, #d8cfc4 100%); }

  .content-panel {
    position: absolute; top: 385px; left: 0; width: 100%; height: 277px;
    background: var(--white);
  }
  .content-panel__strip {
    position: absolute; top: 0; right: 0; width: 280px; height: 9px;
    background: var(--orange);
    clip-path: polygon(0 0, 100% 0, 100% 100%, 4% 100%);
  }

  .orange-card {
    position: absolute; left: 0; width: 223px;
    background: var(--orange); color: var(--white);
    border-top-right-radius: 12px;
  }
  .orange-card--intro { top: 351px; height: 240px; padding: 19px 8px 0 18px; }
  .orange-card--offer { top: 372px; height: 340px; width: 225px; padding: 20px 10px 0 11px; }

  .intro__kicker { font-family: var(--serif); font-size: 13px; line-height: 1.2; color: var(--charcoal); }
  .intro__title {
    font-family: var(--serif); font-weight: 400; font-size: 17.5px; line-height: 1.15;
    color: var(--charcoal); margin-top: 2px; white-space: nowrap;
  }
  .intro__sub { font-family: var(--serif); font-size: 14px; line-height: 1.2; color: var(--charcoal); margin-top: 2px; }
  .rule { width: 54px; height: 2px; background: var(--charcoal); margin: 5px 0 22px; }
  .rule--tight { margin: 5px 0 11px; }
  .intro__text { font-size: 9px; line-height: 1.3; font-weight: 400; text-align: justify; }
  .intro__text + .intro__text { margin-top: 11px; }

  .benefits {
    position: absolute; top: 410px; left: 236px; width: 312px; list-style: none;
    font-size: 9px; line-height: 1.3; color: var(--body-grey); font-weight: 300; text-align: justify;
  }
  .benefits li + li { margin-top: 12px; }

  .gallery {
    position: absolute; top: 597px; left: 16px; width: 528px; height: 105px;
    display: grid; grid-template-columns: repeat(4, 1fr); gap: 4px;
  }
  .thumb { width: 100%; height: 100%; }
  .thumb--hall { background: linear-gradient(160deg, #e8e4dd, #8a7a64); }
  .thumb--bedroom { background: linear-gradient(160deg, #f1efe9, #9aa6a0); }
  .thumb--bath { background: linear-gradient(160deg, #dcd8d1, #b7ab9a); }
  .thumb--exterior { background: linear-gradient(180deg, #7a86a8, #d9cfc4 60%, #5e5650); }

  .cta-heading {
    position: absolute; top: 728px; left: 0; width: 100%; text-align: center;
    font-family: var(--serif); font-size: 15px; color: var(--white); letter-spacing: 0.2px;
  }
  .contact-pill {
    position: absolute; top: 758px; left: 113px; width: 334px; height: 20px;
    background: var(--orange); border-radius: 10px; color: var(--white);
    display: flex; align-items: center; justify-content: center; gap: 18px;
    font-size: 8px;
  }
  .contact-pill__item { display: flex; align-items: center; gap: 5px; }
  .contact-pill svg { width: 9px; height: 9px; }

  .section-title {
    font-family: var(--serif); font-weight: 400; font-size: 18px; line-height: 1.2; color: var(--charcoal);
  }
  .offer-list { list-style: none; font-size: 9px; line-height: 1.25; text-align: justify; }
  .offer-list li + li { margin-top: 7px; }
  .offer-list + .section-title { margin-top: 18px; }

  .how-it-works { position: absolute; top: 396px; left: 244px; width: 306px; }
  .how-it-works .section-title { text-align: right; font-size: 17.5px; }
  .how-it-works__text {
    margin-top: 4px; font-size: 9px; line-height: 1.25; color: var(--body-grey);
    font-weight: 300; text-align: center;
  }
  .showcase {
    position: absolute; top: 470px; left: 238px; width: 311px; height: 232px;
    display: grid; grid-template-columns: 1fr 1fr; grid-template-rows: 1fr 1fr; gap: 8px 6px;
  }
  .tile--living { background: linear-gradient(150deg, #3b4450, #1f2328); }
  .tile--cottage { background: linear-gradient(180deg, #9cb4d0, #5c5a52 55%, #5f8a3e); }
  .tile--coast { background: linear-gradient(180deg, #c9b8c8, #6d87a3 55%, #3e5a36); }
  .tile--deck { background: linear-gradient(180deg, #dfe6ea, #b39a7e 70%, #8a6d52); }
</style>
</head>
<body>

<section class="page page--front" aria-label="Flyer front">
  <header class="brand"><span class="brand__name">KEN DALTON</span></header>
  <div class="accent-bar"></div>
  <div class="hero hero--lounge" role="img" aria-label="Photo of a timber-lined living room with a hanging fireplace and large windows at dusk"></div>
  <div class="content-panel"><div class="content-panel__strip"></div></div>

  <div class="orange-card orange-card--intro">
    <p class="intro__kicker">Welcome to</p>
    <h1 class="intro__title">THE KLD REAL<br>ESTATE PHOTOGRAPHY</h1>
    <p class="intro__sub">Editing and Support Service</p>
    <div class="rule"></div>
    <p class="intro__text">The KLD Real Estate Photography Editing and Support Service is the perfect solution for busy real estate professionals who want to take their business to the next level.</p>
    <p class="intro__text">Our service is affordable, flexible, and designed to help you showcase your listings in the best possible light.</p>
  </div>

  <ul class="benefits">
    <li>• Take your real estate business to the next level by providing impressive real estate imagery that makes you stands out from the competition</li>
    <li>• Omit the stress of trying to find a good photographer or managing an unreliable one and hence have more time to focus on other aspects of your business</li>
    <li>• Showcase your listings with better quality and more impactful photographs than your competitors thereby increasing potential for a quick sale</li>
    <li>• Great first impressions matter and you will achieve this by looking and feeling more professional. This will attract and retain more future clients.</li>
  </ul>

  <div class="gallery">
    <div class="thumb thumb--hall" role="img" aria-label="Photo of a bright hallway with framed art"></div>
    <div class="thumb thumb--bedroom" role="img" aria-label="Photo of a light bedroom with a valley view"></div>
    <div class="thumb thumb--bath" role="img" aria-label="Photo of a stone bathroom with a freestanding bath"></div>
    <div class="thumb thumb--exterior" role="img" aria-label="Photo of a gabled house exterior at twilight"></div>
  </div>

  <p class="cta-heading">CONTACT US TODAY TO LEARN MORE ABOUT HOW WE CAN HELP YOU.</p>
  <div class="contact-pill">
    <span class="contact-pill__item">Contact Us NOW!</span>
    <span class="contact-pill__item">
      <svg viewBox="0 0 10 10"><circle cx="5" cy="5" r="5" fill="#2c2c2d"/><path d="M3.3 2.6l1 1-.5.6c.3.7.8 1.2 1.5 1.5l.6-.5 1 1-.7.8c-1.7-.3-3.4-2-3.7-3.7z" fill="#fff"/></svg>
      0412 555 019
    </span>
    <span class="contact-pill__item">
      <svg viewBox="0 0 10 10"><circle cx="5" cy="5" r="5" fill="#2c2c2d"/><rect x="2.6" y="3.3" width="4.8" height="3.4" fill="none" stroke="#fff" stroke-width=".7"/><path d="M2.6 3.3L5 5.2l2.4-1.9" fill="none" stroke="#fff" stroke-width=".7"/></svg>
      info@kendalton.com.au
    </span>
  </div>
</section>

<section class="page page--back" aria-label="Flyer back">
  <header class="brand"><span class="brand__name">KEN DALTON</span></header>
  <div class="accent-bar"></div>
  <div class="hero hero--kitchen" role="img" aria-label="Photo of a white open-plan kitchen and dining room with dark timber beams"></div>
  <div class="content-panel"><div class="content-panel__strip"></div></div>

  <div class="orange-card orange-card--offer">
    <h2 class="section-title">INCLUSIONS</h2>
    <div class="rule rule--tight"></div>
    <ul class="offer-list">
      <li>• Full day face to face training (we come to you) and instructional handbook</li>
      <li>• We will teach you everything you need to know about your equipment and how to take stunning real estate photographs</li>
      <li>• Service turnaround within 1 working day</li>
      <li>• Free HELP desk service Mon-Fri</li>
      <li>• 12 month Exclusivity (rural towns only) for a limited time</li>
    </ul>
    <h2 class="section-title">INVESTMENT</h2>
    <div class="rule rule--tight"></div>
    <ul class="offer-list">
      <li>• 99 per listing for us to manage images including editing, quality control and delivery (10 Images)</li>
      <li>• Ask us about competitive packages for photography equipment if required</li>
    </ul>
  </div>

  <div class="how-it-works">
    <h2 class="section-title">HOW IT WORKS</h2>
    <p class="how-it-works__text">We understand that your time is valuable, so let us handle the editing and delivery of your images. You shoot, and we take care of the rest. Images are edited and delivered within 1 working day</p>
  </div>

  <div class="showcase">
    <div class="tile--living" role="img" aria-label="Photo of a dark living room with a leather sofa"></div>
    <div class="tile--cottage" role="img" aria-label="Photo of a dark cottage with a garden path at dusk"></div>
    <div class="tile--coast" role="img" aria-label="Photo of a black cabin on a coastal cliff"></div>
    <div class="tile--deck" role="img" aria-label="Photo of a timber deck with outdoor seating"></div>
  </div>

  <p class="cta-heading">CONTACT US TODAY TO LEARN MORE ABOUT HOW WE CAN HELP YOU.</p>
  <div class="contact-pill">
    <span class="contact-pill__item">Contact Us NOW!</span>
    <span class="contact-pill__item">
      <svg viewBox="0 0 10 10"><circle cx="5" cy="5" r="5" fill="#2c2c2d"/><path d="M3.3 2.6l1 1-.5.6c.3.7.8 1.2 1.5 1.5l.6-.5 1 1-.7.8c-1.7-.3-3.4-2-3.7-3.7z" fill="#fff"/></svg>
      0412 555 019
    </span>
    <span class="contact-pill__item">
      <svg viewBox="0 0 10 10"><circle cx="5" cy="5" r="5" fill="#2c2c2d"/><rect x="2.6" y="3.3" width="4.8" height="3.4" fill="none" stroke="#fff" stroke-width=".7"/><path d="M2.6 3.3L5 5.2l2.4-1.9" fill="none" stroke="#fff" stroke-width=".7"/></svg>
      info@kendalton.com.au
    </span>
  </div>
</section>

</body>
</html>
```